Christmas Postcard a manufacturer of skirting boards

Relaunch of the Christmas greetings Postcard of a company manufacturing premium quality skirting boards from real wood. Please refer to http://www.brumholt-profile.example/

- Christmas greetings Postcard 105 mm x 210 mm (card will be sent without envelope)

frontside:
- your graphic design, including
- Logo on the card
- Greetings "Frohe Weihnachten und ein erfolgreiches neues Jahr" on the card (front)
- insert Wooden Earring(s) - for recognition!

backside: (on the left)
"Wir bedanken uns für die partnerschaftliche Zusammenarbeit und freuen uns darauf, Sie auch im Jahr 2016 mit unseren Angeboten, Ideen und Know-how bei der Verwirklichung Ihrer Vorhaben zu unterstützen. (see pdf´s)

Ihnen und Ihren Mitarbeitern wünschen wir ein zauberhaftes Weihnachtsfest und für das neue Jahr Gesundheit, Glück, Erfolg und Freude."

Signatures (see pdf`s)

backside (on the right):
Adress field

------
The pdf´s from last years are just for the color mood. Fresh, modern design appreciated, no comic style.

Industry/Entity Type

It Company

Requirements
Must have
• "Wooden Earring(s)"

```html
<!DOCTYPE html>
<html lang="de">
<head>
<meta charset="utf-8">
<title>Brumholt – Weihnachtskarte</title>
<link href="https://fonts.googleapis.com/css2?family=Orbitron:wght@600;700&family=Questrial&family=Jost:wght@400&display=swap" rel="stylesheet">
<style>
  :root {
    --backdrop: #bcbdbf;
    --paper: #ffffff;
    --brand-red: #b8323f;
    --brand-tan: #e3b78c;
    --ink-dark: #3a2a22;
    --wood-dark: #3a1b10;
    --wood-mid: #5a2d1a;
    --wood-light: #6f3b24;
    --photo-skin: #efd5c2;
    --photo-red: #c62129;
    --photo-red-deep: #a5161f;
    --earring-wood: #6a3a22;
    --earring-wood-light: #9a6040;
    --text-light: #ffffff;
  }
  * { margin: 0; padding: 0; box-sizing: border-box; }
  html, body { width: 1198px; height: 1200px; overflow: hidden; background: var(--backdrop); }
  .canvas { position: relative; width: 1198px; height: 1200px; }
  .card { position: absolute; left: 136px; top: 137px; width: 925px; height: 925px; background: var(--paper); overflow: hidden; }

  .hero-photo {
    position: absolute; left: 340px; top: 0; width: 585px; height: 463px;
    background: linear-gradient(180deg, #f3ded0 0%, var(--photo-skin) 35%, #dc7e74 58%, var(--photo-red) 75%, var(--photo-red-deep) 100%);
    -webkit-mask-image: linear-gradient(90deg, transparent 0%, #000 22%);
    mask-image: linear-gradient(90deg, transparent 0%, #000 22%);
  }
  .earring {
    position: absolute; left: 570px; top: 168px; width: 32px; height: 86px;
    border-radius: 14px;
    background: linear-gradient(160deg, var(--earring-wood-light), var(--earring-wood) 60%, #4a2615);
  }

  .brand-band { position: absolute; left: 0; top: 100px; width: 299px; height: 94px; }
  .brand-band .rule { height: 6px; background: var(--brand-red); }
  .brand-band .field { height: 88px; background: var(--brand-tan); position: relative; }
  .brand-name {
    position: absolute; left: 46px; top: 18px;
    display: flex; align-items: center; gap: 10px;
    font-family: "Orbitron", sans-serif; font-weight: 700; font-size: 30px; line-height: 1;
    color: var(--paper); letter-spacing: 1px;
  }
  .brand-name .mark { width: 20px; height: 20px; background: var(--brand-red); }
  .brand-tagline {
    position: absolute; left: 46px; top: 63px;
    font-family: "Jost", sans-serif; font-size: 14px; letter-spacing: 2px; line-height: 1; color: var(--ink-dark);
  }

  .greeting {
    position: absolute; left: 47px; top: 199px;
    font-family: "Orbitron", sans-serif; font-weight: 600; font-size: 27px;
    line-height: 39.5px; color: var(--brand-red); text-transform: uppercase; letter-spacing: 0;
  }

  .wood-panel {
    position: absolute; left: 0; top: 463px; width: 925px; height: 462px;
    background:
      linear-gradient(178deg, rgba(0,0,0,0.10) 0%, rgba(255,255,255,0.03) 18%, rgba(0,0,0,0.06) 34%, rgba(255,255,255,0.04) 52%, rgba(0,0,0,0.08) 70%, rgba(255,255,255,0.02) 86%, rgba(0,0,0,0.12) 100%),
      radial-gradient(ellipse 70% 60% at 50% 50%, var(--wood-light), var(--wood-mid) 60%, var(--wood-dark));
  }
  .message {
    position: absolute; left: 0; top: 158px; width: 925px; text-align: center;
    font-family: "Questrial", sans-serif; font-size: 17.5px; line-height: 23px; color: var(--text-light);
  }
  .message .divider { width: 682px; margin: 12px auto 13px; border-top: 1px dotted rgba(255,255,255,0.8); }
</style>
</head>
<body>
<div class="canvas">
  <div class="card">
    <div class="hero-photo" role="img" aria-label="Photo of a smiling woman in a red Santa costume with falling red gift boxes and a wrapped present"></div>
    <div class="earring" role="img" aria-label="Wooden S-shaped earring worn by the woman"></div>

    <div class="brand-band">
      <div class="rule"></div>
      <div class="field">
        <div class="brand-name"><span class="mark"></span>Brumholt</div>
        <div class="brand-tagline">Leistenfabrik Holzimport</div>
      </div>
    </div>

    <h1 class="greeting">Frohe<br>Weihnachten<br>und ein<br>erfolgreiches<br>neues Jahr</h1>

    <div class="wood-panel" role="img" aria-label="Dark wood grain background">
      <div class="message">
        <p>Wir bedanken uns für die partnerschaftliche Zusammenarbeit und freuen<br>uns darauf, Sie auch im Jahr 2016 mit unseren Angeboten,<br>Ideen und Know-how bei der Verwirklichung Ihrer Vorhaben zu unterstützen.</p>
        <div class="divider"></div>
        <p>Ihnen und Ihren Mitarbeitern wünschen wir ein zauberhaftes Weihnachtsfest und<br>für das neue Jahr Gesundheit, Glück, Erfolg und Freude.</p>
      </div>
    </div>
  </div>
</div>
</body>
</html>
```